National Teen and Tween Athletic Business Needs Banner Designs for Breast Cancer Awareness Month

We need a series of two to four (2-4) of simple and impactful banners for our website carousel (see www.ferncrestathletica.com) in size 901 wide by 444 tall (anything close is ok).

It is for a breast cancer donation we were able to negotiate with our factory just this past Thursday.

If we pre-sell 2500 bras in two weeks we can donate $25,000 to breast cancer research

On Friday a colleague and I separately video’d 10 second messages saying that we worked out a deal with our factory to make 2500 seamless sprinter bras, which is one production run, in white with pink. We held up the white/ lime color (see http://www.ferncrestathletica.com/bras/the-sprinter.html) (http://www.ferncrestathletica.com/catalog/product/gallery/id/248/image/430/pid/273/) and described it would be white with pink and that if we sold 2,500 we could do one production run and donate $25000 to breast cancer research.

I did record a second message that mentioned we would contribute to Norah’s Lab. Dr Norah Pembrook worldwide breast cancer specialist at Halvick Institute in North Carolina. Then there is a call to action “lets do it!”

We'd like to make banners for the website.

Designers, we'd appreciate your advice on if we can link or use the video's in one of the carousel banners.

If you want to purchase a photo on snapvault or other photo service, please use it with the watermark on your design and if you are the winner, direct us to the photo and we can buy it.

(The below messaging could be one banner, three or four)

First message:
Starting October 17th:
A two week campaign
To sell 2,500 bras
To raise $25,000 for breast cancer
Let's do it!

I’d like to do a Ferncrest Honor and Memory wall banner where-whether you buy a bra or not, folks can list someone to honor or remember. One of our investors, Marta Delphos, is a breast cancer survivor and our finance person, Ruth Okonkwo’s mother, Ilse Brennick, passed away in 1990 at age 51 from breast cancer. We would like to be able to keep adding names to this and update it daily.

Target Market(s)

Girls ages 10-17 and their parents and coaches. Our customer is a serious athletic girl, think of Tamsin Holloway from Ember Trials and Jo Perrin, soccer star.

Industry/Entity Type

Business

Font styles to use
Sans Serif

Colors
f8d9e8
fbd3d4
f59195
e34297
e567a6
eea4c8

Requirements
Must have
• a breast cancer awareness ribbon, the ferncrest logo. Clear and simple -impactful.
Nice to have
• If it works with your design and is impactful, add images of athletic girls in action. Not essential. The most important thing is that the call to action is compelling.

```html
<!DOCTYPE html>
<html lang="en">
<head>
<meta charset="utf-8">
<title>Ferncrest Athletica Breast Cancer Awareness Banner</title>
<link rel="stylesheet" href="https://fonts.googleapis.com/css2?family=Comfortaa:wght@300;700&display=swap">
<style>
  :root {
    --salmon: #f28c98;
    --rose: #e567a6;
    --magenta: #dd3f98;
    --white: #ffffff;
    --brand-ink: #e34297;
    --ribbon-pink: #f060b8;
    --ribbon-light: #f7a6d6;
    --ribbon-faint: rgba(255, 255, 255, 0.12);
  }
  html, body {
    margin: 0;
    padding: 0;
    overflow: hidden;
    background: var(--white);
  }
  .banner {
    position: relative;
    width: 1200px;
    height: 591px;
    overflow: hidden;
    background: linear-gradient(90deg, var(--salmon) 0%, var(--rose) 45%, var(--magenta) 100%);
    font-family: "Comfortaa", sans-serif;
    color: var(--white);
  }
  .top-edge {
    position: absolute;
    left: 0;
    top: 0;
    width: 952px;
    height: 6px;
    background: var(--white);
  }
  .logo-tab {
    position: absolute;
    left: 0;
    top: 0;
    width: 360px;
    height: 92px;
    background: var(--white);
    border-bottom-right-radius: 60px;
  }
  .logo-tab::after {
    content: "";
    position: absolute;
    left: 0;
    top: 92px;
    width: 14px;
    height: 110px;
    background: var(--white);
    border-bottom-right-radius: 14px;
  }
  .brand {
    position: absolute;
    left: 34px;
    top: 26px;
    display: flex;
    align-items: center;
    gap: 10px;
    font-weight: 700;
    font-size: 24px;
    color: var(--brand-ink);
    white-space: nowrap;
  }
  .brand-dot {
    width: 14px;
    height: 14px;
    border-radius: 50%;
    background: var(--brand-ink);
  }
  .ribbon {
    position: absolute;
    border-radius: 50% 50% 18% 18%;
  }
  .ribbon-feature {
    left: 56px;
    top: 334px;
    width: 222px;
    height: 257px;
    background: linear-gradient(160deg, var(--ribbon-light), var(--ribbon-pink));
  }
  .ribbon-ghost-large {
    left: 812px;
    top: 40px;
    width: 334px;
    height: 551px;
    background: var(--ribbon-faint);
  }
  .ribbon-ghost-top {
    left: 594px;
    top: 54px;
    width: 78px;
    height: 132px;
    background: rgba(255, 255, 255, 0.08);
  }
  .ribbon-ghost-left {
    left: 300px;
    top: 300px;
    width: 58px;
    height: 86px;
    background: rgba(255, 255, 255, 0.08);
  }
  .message {
    position: absolute;
    left: 0;
    width: 1176px;
    top: 154px;
    text-align: center;
  }
  .campaign-details {
    margin: 0;
    font-weight: 300;
    font-size: 30.5px;
    line-height: 41px;
  }
  .call-to-action {
    margin: -4px 0 0;
    font-weight: 300;
    font-size: 114px;
    line-height: 1;
    letter-spacing: 1px;
  }
</style>
</head>
<body>
  <main class="banner">
    <div class="top-edge"></div>
    <div class="logo-tab">
      <div class="brand">Ferncrest Athletica <span class="brand-dot"></span></div>
    </div>

    <div class="ribbon ribbon-ghost-large" role="img" aria-label="Large faint pink awareness ribbon"></div>
    <div class="ribbon ribbon-ghost-top" role="img" aria-label="Small faint awareness ribbon"></div>
    <div class="ribbon ribbon-ghost-left" role="img" aria-label="Small faint awareness ribbon"></div>
    <div class="ribbon ribbon-feature" role="img" aria-label="Bright pink breast cancer awareness ribbon"></div>

    <section class="message">
      <p class="campaign-details">
        Starting October 17th:<br>
        A two week campaign<br>
        To sell 2,500 bras To raise $25,000<br>
        for breast cancer
      </p>
      <h1 class="call-to-action">Let's do it!</h1>
    </section>
  </main>
</body>
</html>
```